Business Card Design - Carrington Hill Lodge

We are looking at a new design for our business cards that has a modern and professional look. We run a residential aged care facility focussing on the care of residents. The cards will be used for potential clients, consultants and business opportunities in this sector. Blue and white is our main colours and would to see these colours incorporated in the design.
Industry/Entity Type
Business
Contact Information for Business Card
Carrington Hill Lodge, Darren Pelham, dpelham@carringtonhilllodge.com.au, Finance Manager, 0491 736 208, BCom, 48 Yarrabee Way, Wattle Ridge, Qld 4521.

```html
<!DOCTYPE html>
<html lang="en">
<head>
<meta charset="utf-8">
<title>Carrington Hill Lodge – Business Card</title>
<link href="https://fonts.googleapis.com/css2?family=Open+Sans:wght@400;600;700&display=swap" rel="stylesheet">
<style>
  :root {
    --stage: #e9e6e2;
    --card: #ffffff;
    --brand-blue: #4f7c98;
    --ink-blue: #3d6a87;
    --shadow: rgba(40, 30, 20, 0.18);
  }
  * { box-sizing: border-box; margin: 0; padding: 0; }
  html, body {
    width: 1200px; height: 1000px; overflow: hidden;
    background: var(--stage);
  }
  .canvas {
    position: relative; width: 1200px; height: 1000px;
    font-family: "Open Sans", Arial, sans-serif;
    color: var(--ink-blue);
  }
  .card {
    position: absolute; left: 265px; width: 665px; height: 398px;
    background: var(--card); border-radius: 22px; overflow: hidden;
    box-shadow: 0 6px 18px var(--shadow);
  }
  .card--front { top: 73px; }
  .card--back  { top: 532px; }

  .band { position: absolute; left: 0; right: 0; height: 19px; background: var(--brand-blue); }
  .band--top { top: 0; }
  .band--bottom { bottom: 0; }

  .contact { position: absolute; left: 33px; top: 108px; }
  .contact__name { font-size: 21px; font-weight: 700; letter-spacing: 0.3px; line-height: 1; }
  .contact__role { font-size: 17px; font-weight: 400; margin-top: 5px; }
  .divider {
    position: absolute; left: 0; top: 174px; width: 34px; height: 2px;
    background: var(--brand-blue);
  }
  .details { position: absolute; left: 33px; top: 195px; font-size: 17px; line-height: 25px; }
  .details__phone { display: flex; align-items: center; gap: 7px; }
  .details__phone svg { width: 13px; height: 13px; fill: var(--ink-blue); }
  .details__address { margin-top: 10px; line-height: 23px; }

  .brand {
    position: absolute; display: flex; flex-direction: column; align-items: center;
    text-align: center; color: var(--brand-blue);
  }
  .brand__dot {
    width: 120px; height: 120px; border-radius: 50%; background: var(--brand-blue);
    margin-bottom: 22px;
  }
  .brand__name {
    font-size: 17px; font-weight: 600; letter-spacing: 1px; text-transform: uppercase;
    line-height: 1.2; white-space: nowrap;
  }
  .card--front .brand { left: 344px; top: 110px; width: 300px; }
  .card--back .brand { left: 132px; top: 82px; width: 400px; }
  .card--back .brand__dot { width: 150px; height: 150px; margin-bottom: 28px; }
  .card--back .brand__name { font-size: 21px; letter-spacing: 1.2px; }
</style>
</head>
<body>
<main class="canvas">
  <section class="card card--front" aria-label="Business card front">
    <div class="band band--top"></div>
    <div class="contact">
      <p class="contact__name">DARREN PELHAM</p>
      <p class="contact__role">Finance Manager</p>
    </div>
    <div class="divider"></div>
    <div class="details">
      <p class="details__phone">
        <svg viewBox="0 0 24 24" aria-hidden="true"><path d="M6.6 10.8a15.1 15.1 0 0 0 6.6 6.6l2.2-2.2a1 1 0 0 1 1-.25 11.4 11.4 0 0 0 3.6.57 1 1 0 0 1 1 1V20a1 1 0 0 1-1 1A17 17 0 0 1 3 4a1 1 0 0 1 1-1h3.5a1 1 0 0 1 1 1c0 1.25.2 2.45.57 3.57a1 1 0 0 1-.25 1z"/></svg>
        0491 736 208
      </p>
      <p class="details__email">dpelham@carringtonhilllodge.com.au</p>
      <p class="details__address">BCom, 48 Yarrabee Way,<br>Wattle Ridge, Qld 4521.</p>
    </div>
    <div class="brand">
      <div class="brand__dot"></div>
      <p class="brand__name">Carrington Hill Lodge</p>
    </div>
    <div class="band band--bottom"></div>
  </section>

  <section class="card card--back" aria-label="Business card back">
    <div class="brand">
      <div class="brand__dot"></div>
      <p class="brand__name">Carrington Hill Lodge</p>
    </div>
  </section>
</main>
</body>
</html>
```